BRAYLEN AT HEARTH, LLC Webpage portfolio

I want to create a Website that allows my potential clients to browse my Skilled work via before and after photos. I want the website to enhance the work that I provide and potentially drive new business, or at least solidify my work.
I also do 3D CAD and Modeling of New Spaces and it would be nice to show some of that work from pencil design to 3D modeling, which I feel may help give me more clients.

The website needs to show a solid carpenter/company with the skills to get any project completed.

Types of Jobs - Custom Carpentry & Finishes, Kitchens, Baths, Basements, Decks, Porches, Whole House Renovation - Skilled Craftsmanship (Hardwood Flooring, Floor and Wall Tile) and much more...

Target Market(s)

Residential Home Renovation, Kitchen and Bath Renovation, Home Improvement

Industry/Entity Type

Residential Construction

Number of Pages Required

5+ page

Font styles to use
Sans Serif
Script

Requirements
Must have
• Similar to Nestlyra.com, except for Braylen At Hearth.
• Must be inviting.
• My Services Offered
• A way to reach me or contact me for estimates with some sort of Screening Questionare.
Nice to have
• Inviting Colors
Should not have
• Not sure at this time

```html
<!DOCTYPE html>
<html lang="en">
<head>
<meta charset="utf-8">
<title>Braylen At Hearth</title>
<link href="https://fonts.googleapis.com/css2?family=Questrial&display=swap" rel="stylesheet">
<style>
:root{
  --blue:#1b9ad6;
  --navy:#0c3c5e;
  --navy-deep:#093250;
  --ink:#1f3a52;
  --text:#6b6f74;
  --line:#dfe3e7;
  --soft:#f4f5f6;
  --white:#ffffff;
}
*{box-sizing:border-box;margin:0;padding:0}
html,body{width:1200px;height:3346px;overflow:hidden}
body{font-family:"Questrial",sans-serif;color:var(--text);background:var(--white);position:relative}
.abs{position:absolute}
a{color:inherit;text-decoration:none}

/* header */
.site-header{position:absolute;left:0;top:0;width:1200px;height:92px;background:var(--white)}
.brand{position:absolute;left:158px;top:30px;display:flex;align-items:center;gap:10px;font-size:19px;color:var(--navy)}
.brand-mark{width:18px;height:18px;background:var(--navy)}
.nav{position:absolute;left:355px;top:34px;font-size:14px;color:var(--ink)}
.nav a{position:absolute;white-space:nowrap}
.nav a.active{color:var(--blue)}
.nav a.active::after{content:"";position:absolute;left:0;right:0;bottom:-12px;height:2px;background:var(--blue)}
.btn-estimate{position:absolute;left:915px;top:26px;width:128px;height:34px;border-radius:17px;background:var(--blue);color:#fff;font-size:13px;display:flex;align-items:center;justify-content:center}

/* hero */
.hero{position:absolute;left:0;top:92px;width:1200px;height:400px;overflow:hidden}
.hero-photo{position:absolute;inset:0;background:
  radial-gradient(ellipse 260px 110px at 880px 250px,rgba(200,200,200,.55),transparent 70%),
  radial-gradient(ellipse 700px 120px at 420px 300px,rgba(170,140,110,.75),transparent 70%),
  linear-gradient(180deg,#2a1c14 0%,#4b3526 30%,#6b5140 55%,#8a7260 68%,#3a271b 82%,#22160f 100%)}
.hero-shade{position:absolute;inset:0;background:rgba(10,10,10,.28)}
.hero-title{position:absolute;left:0;width:1200px;top:120px;text-align:center;color:#fff;font-size:36px;line-height:46px;font-weight:400}
.btn-ghost-light{position:absolute;left:535px;top:232px;width:130px;height:34px;border:2px solid #fff;border-radius:17px;color:#fff;font-size:12px;display:flex;align-items:center;justify-content:center}
.hero-arrow{position:absolute;top:185px}

/* about */
.section-title{font-size:28px;color:var(--ink);font-weight:400}
.section-title span{color:var(--blue)}
.about-title{position:absolute;left:156px;top:532px}
.about-title::after{content:"";position:absolute;left:0;top:48px;width:530px;height:1px;background:var(--line)}
.about-photo{position:absolute;left:156px;top:603px;width:532px;height:150px;background:
  radial-gradient(ellipse 120px 80px at 150px 90px,rgba(226,190,70,.9),transparent 70%),
  radial-gradient(ellipse 140px 70px at 380px 60px,rgba(190,150,120,.6),transparent 70%),
  linear-gradient(135deg,#c9c3b8,#e8e4dc 50%,#b8b2a6)}
.about-sub{position:absolute;left:156px;top:770px;font-size:22px;color:var(--blue);display:flex;align-items:center;gap:22px;font-weight:400}
.about-sub::before{content:"";width:36px;height:2px;background:var(--blue)}
.about-text{position:absolute;left:156px;top:812px;width:532px;font-size:12.5px;line-height:20px}
.btn-solid{position:absolute;height:36px;border-radius:18px;background:var(--blue);color:#fff;font-size:12px;display:flex;align-items:center;justify-content:center}
.btn-outline{position:absolute;height:34px;border-radius:17px;border:2px solid var(--blue);color:var(--blue);font-size:12px;display:flex;align-items:center;justify-content:center;background:#fff}

.quote-card{position:absolute;left:763px;top:540px;width:280px;height:437px;background:#fff;box-shadow:0 4px 18px rgba(0,0,0,.14)}
.quote-head{height:90px;background:var(--blue);color:#fff;text-align:center;padding-top:14px}
.quote-head h3{font-size:24px;font-weight:400}
.quote-head p{font-size:11.5px;line-height:16px;margin-top:2px}
.field{position:absolute;left:24px;width:233px;height:33px;border:1px solid var(--line);font-size:11px;color:#a9adb2;padding:9px 10px}

/* services */
.services{position:absolute;left:0;top:1025px;width:1200px;height:475px;background:var(--soft)}
.centered-title{position:absolute;left:0;width:1200px;text-align:center}
.centered-title::after{content:"";display:block;width:48px;height:2px;background:var(--blue);margin:10px auto 0}
.service-card{position:absolute;top:107px;width:280px;height:323px;background:#fff;box-shadow:0 2px 8px rgba(0,0,0,.08)}
.service-photo{height:174px;position:relative}
.service-label{position:absolute;left:0;right:0;bottom:0;height:30px;background:rgba(20,30,40,.7);color:#fff;font-size:14px;padding:7px 22px}
.service-label.highlight{background:var(--blue)}
.service-text{position:absolute;left:24px;top:194px;width:232px;font-size:12px;line-height:18px}
.read-more{position:absolute;left:24px;top:287px;font-size:12px;color:var(--ink);display:flex;align-items:center;gap:8px}
.read-more::before{content:"";width:5px;height:5px;border-radius:50%;background:var(--ink)}
.read-more.highlight{color:var(--blue);text-decoration:underline}
.read-more.highlight::before{background:var(--blue)}

/* testimonial */
.testimonial{position:absolute;left:0;top:1500px;width:1200px;height:398px;background:var(--navy);color:#fff}
.avatar{position:absolute;left:537px;top:47px;width:126px;height:126px;border-radius:50%;border:4px solid #fff;background:
  radial-gradient(ellipse 60px 40px at 60px 125px,#1d2a4a,transparent 80%),
  linear-gradient(180deg,#eef1f4 0%,#d8dde2 45%,#2a3552 100%)}
.quote-text{position:absolute;left:230px;top:205px;width:740px;text-align:center;font-size:13.5px;line-height:22px}
.quote-divider{position:absolute;left:535px;top:275px;width:130px;height:30px}
.cite-name{position:absolute;left:0;width:1200px;top:313px;text-align:center;font-size:17px}
.cite-role{position:absolute;left:0;width:1200px;top:337px;text-align:center;font-size:11px;color:#c9d6e0}

/* blog */
.blog-card{position:absolute;top:1998px;height:494px;background:#fff;border:1px solid #eceef0}
.blog-card.raised{box-shadow:0 4px 16px rgba(0,0,0,.16);border:none}
.blog-photo{position:absolute;left:25px;top:27px;right:25px;height:160px}
.blog-date{position:absolute;left:25px;top:172px;height:26px;padding:6px 14px;background:var(--blue);color:#fff;font-size:11px}
.blog-title{position:absolute;left:20px;right:20px;top:217px;text-align:center;color:var(--ink);font-size:16px;line-height:22px;font-weight:400}
.blog-text{position:absolute;left:32px;right:32px;top:270px;text-align:center;font-size:12px;line-height:18px}
.blog-meta{position:absolute;left:0;right:0;top:377px;display:flex;justify-content:center;gap:14px;font-size:10.5px;color:var(--text)}
.blog-meta i{font-style:normal;display:inline-flex;align-items:center;gap:5px}

/* work */
.work{position:absolute;left:0;top:2540px;width:1200px;height:475px;background:var(--soft)}
.work-frame{position:absolute;top:107px;width:353px;height:238px;background:#e2e4e6}
.work-half{position:absolute;top:10px;width:164px;height:218px}
.work-tag{position:absolute;left:0;right:0;bottom:0;height:34px;background:rgba(10,25,35,.75);color:#fff;font-size:13px;padding:10px 14px}

/* footer */
.footer{position:absolute;left:0;top:3015px;width:1200px;height:275px;background:var(--navy);color:#fff}
.footer h4{position:absolute;top:42px;font-size:17px;font-weight:400}
.footer-col-text{position:absolute;font-size:11.5px;line-height:17px;color:#cfdbe4}
.footer-divider{position:absolute;top:40px;width:1px;height:200px;background:rgba(255,255,255,.2)}
.social{position:absolute;left:156px;top:195px;display:flex;gap:8px}
.social span{width:28px;height:28px;border-radius:50%;background:var(--blue);border:2px solid var(--blue)}
.news-input{position:absolute;left:535px;top:140px;width:282px;height:30px;border-bottom:1px solid rgba(255,255,255,.35);font-size:12px;color:#dbe5ec;padding-top:8px}
.quick-links{position:absolute;left:915px;top:80px;font-size:12px;line-height:29px;color:#cfdbe4;list-style:none}
.quick-links li::before{content:"› ";color:var(--blue)}
.quick-links li.active{color:var(--blue)}
.copyright{position:absolute;left:0;top:3290px;width:1200px;height:56px;background:var(--navy-deep);color:#cfdbe4;font-size:11px}
</style>
</head>
<body>

<header class="site-header">
  <div class="brand"><span class="brand-mark"></span>Braylen At Hearth</div>
  <nav class="nav">
    <a class="active" style="left:0">Home</a>
    <a style="left:85px">About Us</a>
    <a style="left:188px">Services</a>
    <a style="left:287px">Work</a>
    <a style="left:364px">Blog</a>
    <a style="left:434px">Contact Us</a>
  </nav>
  <a class="btn-estimate">Free Estimate</a>
</header>

<section class="hero">
  <div class="hero-photo" role="img" aria-label="Photo of a renovated kitchen with granite countertop and steel sink"></div>
  <div class="hero-shade"></div>
  <svg class="hero-arrow" style="left:108px" width="26" height="22" viewBox="0 0 26 22"><path d="M10 2 L2 9 L10 16 M2 9 H16 Q24 9 24 20" fill="none" stroke="#fff" stroke-width="3"/></svg>
  <svg class="hero-arrow" style="left:1066px" width="26" height="22" viewBox="0 0 26 22"><path d="M16 2 L24 9 L16 16 M24 9 H10 Q2 9 2 20" fill="none" stroke="#1b9ad6" stroke-width="3"/></svg>
  <h1 class="hero-title">The New Way To Design<br>Your Home</h1>
  <a class="btn-ghost-light">Explore More</a>
</section>

<h2 class="section-title about-title">Braylen <span>At</span> Hearth</h2>
<div class="about-photo" role="img" aria-label="Illustration of a model house beside paint colour swatches"></div>
<h3 class="about-sub">About Us</h3>
<p class="about-text">There are many variations of passages of Lorem Ipsum available, but the majority have suffered alteration in some form, by injected humour, or randomised words which don't look even slightly believable. If you are going to use a passage of Lorem Ipsum, you need to be sure there isn't anything embarrassing hidden in the middle of text. All the Lorem Ipsum generators on the It is a long established fact that a reader...</p>
<a class="btn-solid" style="left:156px;top:943px;width:130px">Discover More</a>

<aside class="quote-card">
  <div class="quote-head">
    <h3>Get A Quote</h3>
    <p>Enquire now and we call back<br>within 60 minutes!</p>
  </div>
  <div class="field" style="top:112px">Name</div>
  <div class="field" style="top:157px">Email</div>
  <div class="field" style="top:202px">Phone</div>
  <div class="field" style="top:248px;height:115px">Message</div>
  <a class="btn-outline" style="left:24px;top:373px;width:96px;gap:6px">
    <svg width="12" height="12" viewBox="0 0 12 12"><path d="M1 6 L11 1 L8 11 L6 7 Z" fill="#1b9ad6"/></svg>Send</a>
</aside>

<section class="services">
  <h2 class="section-title centered-title" style="top:45px"><span>Our</span> Services</h2>
  <article class="service-card" style="left:156px">
    <div class="service-photo" role="img" aria-label="Photo of a renovated open-plan living room" style="background:radial-gradient(ellipse 110px 60px at 200px 60px,rgba(255,250,240,.9),transparent 70%),linear-gradient(180deg,#d9cfc2 0%,#efe9e0 45%,#a98d6e 75%,#7c6148 100%)">
      <div class="service-label">Home Renovation</div></div>
    <p class="service-text">Lorem Ipsum has been the industry's standard dummy text ever since the 1500s, when an unknown printer took galley of...</p>
    <a class="read-more">Read More</a>
  </article>
  <article class="service-card" style="left:459px">
    <div class="service-photo" role="img" aria-label="Photo of a bright renovated bathroom" style="background:radial-gradient(ellipse 90px 70px at 90px 70px,rgba(255,255,255,.95),transparent 70%),linear-gradient(180deg,#e6e8e8 0%,#f4f2ee 50%,#b9b3a8 80%,#8f887d 100%)">
      <div class="service-label highlight">Kitchen and Bath Renovation</div></div>
    <p class="service-text">Lorem Ipsum has been the industry's standard dummy text ever since the 1500s, when an unknown printer took galley of...</p>
    <a class="read-more highlight">Read More</a>
  </article>
  <article class="service-card" style="left:763px">
    <div class="service-photo" role="img" aria-label="Photo of a dining room with arched doorway" style="background:radial-gradient(ellipse 70px 60px at 200px 80px,rgba(235,240,240,.9),transparent 70%),linear-gradient(180deg,#5c4634 0%,#a88d6c 35%,#d4c2a3 60%,#6e5a44 100%)">
      <div class="service-label">Home Improvement</div></div>
    <p class="service-text">Lorem Ipsum has been the industry's standard dummy text ever since the 1500s, when an unknown printer took galley of...</p>
    <a class="read-more">Read More</a>
  </article>
</section>

<section class="testimonial">
  <div class="avatar" role="img" aria-label="Portrait photo of the client"></div>
  <svg class="abs" style="left:152px;top:200px" width="26" height="22" viewBox="0 0 26 22"><path d="M10 2 L2 9 L10 16 M2 9 H16 Q24 9 24 20" fill="none" stroke="#fff" stroke-width="3"/></svg>
  <svg class="abs" style="left:1020px;top:200px" width="26" height="22" viewBox="0 0 26 22"><path d="M16 2 L24 9 L16 16 M24 9 H10 Q2 9 2 20" fill="none" stroke="#1b9ad6" stroke-width="3"/></svg>
  <p class="quote-text">"Excellent service; quote given on the spot for major clean-up of household throw-outs. The team provides quick, efficient and courteous removal! Very satisfied customer!"</p>
  <svg class="quote-divider" viewBox="0 0 130 30"><path d="M0 15 H45 M85 15 H130" stroke="#1b9ad6" stroke-width="1.5"/><path d="M55 6 h16 a4 4 0 0 1 4 4 v8 a4 4 0 0 1 -4 4 h-9 l-5 5 v-5 h-2 a4 4 0 0 1 -4 -4 v-8 a4 4 0 0 1 4 -4z" fill="none" stroke="#1b9ad6" stroke-width="2"/></svg>
  <div class="cite-name">Marco Ellery - Harbor Point</div>
  <div class="cite-role">- Residential Rubbish</div>
</section>

<h2 class="section-title centered-title" style="top:1943px"><span>Our</span> Latest Blog</h2>

<article class="blog-card" style="left:156px;width:263px">
  <div class="blog-photo" role="img" aria-label="Photo of a house porch with white railings" style="background:radial-gradient(ellipse 80px 50px at 110px 110px,rgba(250,250,248,.9),transparent 70%),linear-gradient(180deg,#c4cacd 0%,#a7adb0 40%,#d8d6cf 65%,#7a7468 100%)"></div>
  <div class="blog-date">25 Oct, 2016</div>
  <h3 class="blog-title">The standard Lorem<br>Ipsum passage</h3>
  <p class="blog-text">There are many variations of passages of Lorem Ipsum available, but the majority have suffered alteration in some form.</p>
  <div class="blog-meta"><i>&#9679; Lorem</i><i>&#9675; 30 Comment</i><i>&lt; Share</i></div>
  <a class="btn-outline" style="left:83px;top:441px;width:96px">Read More</a>
</article>
<article class="blog-card raised" style="left:459px;width:281px">
  <div class="blog-photo" role="img" aria-label="Photo of a wooden kitchen with pendant lights" style="background:radial-gradient(ellipse 60px 30px at 120px 60px,rgba(250,200,130,.75),transparent 70%),linear-gradient(180deg,#2e1c12 0%,#6e4426 40%,#9a6a42 60%,#2a1a10 100%)"></div>
  <div class="blog-date">30 Oct, 2016</div>
  <h3 class="blog-title">The standard Lorem<br>Ipsum passage</h3>
  <p class="blog-text">There are many variations of passages of Lorem Ipsum available, but the majority have suffered alteration in some form.</p>
  <div class="blog-meta"><i>&#9679; Lorem</i><i>&#9675; 30 Comment</i><i>&lt; Share</i></div>
  <a class="btn-solid" style="left:92px;top:441px;width:96px;height:34px">Read More</a>
</article>
<article class="blog-card" style="left:763px;width:280px">
  <div class="blog-photo" role="img" aria-label="Photo of a wood-panelled living room" style="background:radial-gradient(ellipse 60px 50px at 60px 60px,rgba(240,200,150,.7),transparent 70%),linear-gradient(180deg,#5a3018 0%,#a46a3c 40%,#c08a58 60%,#3e2210 100%)"></div>
  <div class="blog-date">05 Jan, 2016</div>
  <h3 class="blog-title">The standard Lorem<br>Ipsum passage</h3>
  <p class="blog-text">There are many variations of passages of Lorem Ipsum available, but the majority have suffered alteration in some form.</p>
  <div class="blog-meta"><i>&#9679; Lorem</i><i>&#9675; 30 Comment</i><i>&lt; Share</i></div>
  <a class="btn-outline" style="left:92px;top:441px;width:96px">Read More</a>
</article>

<section class="work">
  <h2 class="section-title centered-title" style="top:45px"><span>Our</span> Work</h2>
  <svg class="abs" style="left:152px;top:218px" width="26" height="22" viewBox="0 0 26 22"><path d="M10 2 L2 9 L10 16 M2 9 H16 Q24 9 24 20" fill="none" stroke="#8a9096" stroke-width="3"/></svg>
  <svg class="abs" style="left:1020px;top:218px" width="26" height="22" viewBox="0 0 26 22"><path d="M16 2 L24 9 L16 16 M24 9 H10 Q2 9 2 20" fill="none" stroke="#1b9ad6" stroke-width="3"/></svg>
  <div class="work-frame" style="left:232px">
    <div class="work-half" role="img" aria-label="Before photo of a living room" style="left:10px;background:radial-gradient(ellipse 60px 50px at 80px 60px,rgba(250,230,170,.8),transparent 70%),linear-gradient(180deg,#e0b060 0%,#c98a3a 45%,#7a4a20 75%,#3a2414 100%)"><div class="work-tag">Before</div></div>
    <div class="work-half" role="img" aria-label="After photo of a dining room" style="left:179px;background:radial-gradient(ellipse 60px 40px at 90px 40px,rgba(250,250,245,.9),transparent 70%),linear-gradient(180deg,#e6e0d2 0%,#d0aa6e 45%,#8a5a30 75%,#4a2e18 100%)"><div class="work-tag">After</div></div>
    <svg class="abs" style="left:164px;top:100px" width="26" height="26" viewBox="0 0 26 26"><circle cx="13" cy="13" r="13" fill="#1b9ad6"/><path d="M8 18 L18 8 M12 8 H18 V14 M8 12 V18 H14" fill="none" stroke="#fff" stroke-width="1.8"/></svg>
  </div>
  <div class="work-frame" style="left:615px">
    <div class="work-half" role="img" aria-label="Before photo of a house exterior in snow" style="left:10px;background:linear-gradient(180deg,#d2dae0 0%,#b9a6a0 35%,#c99a92 55%,#f0f0f0 80%,#dcdcdc 100%)"><div class="work-tag">Before</div></div>
    <div class="work-half" role="img" aria-label="After photo of a renovated house exterior" style="left:179px;background:linear-gradient(180deg,#dde3e8 0%,#9aa5ae 35%,#c2c8cc 55%,#6f7a58 80%,#55603e 100%)"><div class="work-tag">After</div></div>
  </div>
  <a class="btn-outline" style="left:552px;top:377px;width:96px">View All</a>
</section>

<footer class="footer">
  <h4 style="left:156px">Braylen At Hearth</h4>
  <p class="footer-col-text" style="left:156px;top:82px">Westbrook, NSW<br>Sed ut perspiciatis unde omnis 3456123</p>
  <p class="abs" style="left:156px;top:130px;font-size:17px">Call Us <span style="color:var(--blue)">&#9990;</span> 0400 555 218</p>
  <p class="footer-col-text" style="left:156px;top:160px">info@braylenathearth.com</p>
  <div class="social"><span></span><span></span><span></span><span></span></div>
  <div class="footer-divider" style="left:486px"></div>
  <h4 style="left:535px">Newsletter</h4>
  <p class="footer-col-text" style="left:535px;top:82px;width:282px">Subscribe to our Newsletter to get the latest scoop right to your inbox.</p>
  <div class="news-input">Enter your email</div>
  <a class="btn-outline" style="left:535px;top:191px;width:96px;height:30px;background:transparent;gap:6px;color:#fff">
    <svg width="12" height="12" viewBox="0 0 12 12"><path d="M1 6 L11 1 L8 11 L6 7 Z" fill="#1b9ad6"/></svg>Send</a>
  <div class="footer-divider" style="left:866px"></div>
  <h4 style="left:915px">Quick Link</h4>
  <ul class="quick-links">
    <li class="active">Home</li><li>About</li><li>Services</li><li>Work</li><li>Contact</li>
  </ul>
</footer>

<div class="copyright">
  <p class="abs" style="left:156px;top:22px">© 2017 Braylen At Hearth. All rights reserved</p>
  <svg class="abs" style="left:1026px;top:18px" width="18" height="18" viewBox="0 0 18 18"><path d="M9 16 V3 M3 9 L9 3 L15 9" fill="none" stroke="#1b9ad6" stroke-width="2.5"/></svg>
</div>

</body>
</html>
```